Disability Service Provider needs a flyer

Project Description:
We are seeking a creative and engaging flyer design to promote a twelve week independent living skills program, focusing on key areas such as money management, basic cooking, food safety, and personal well-being and interpersonal skills. The flyer will be used to encourage individuals to enhance their abilities to live independently and confidently.

Target Audience:
Our target audience includes young adults with a disability and individuals transitioning into independent living situations. We aim to reach those who may be new to managing their own finances, cooking for themselves, and maintaining a healthy lifestyle.

Key Messages:

Independent Living Skills: Emphasize the importance of acquiring essential skills for independent living.
Money Management: Highlight budgeting tips, saving strategies, and financial planning.
Basic Cooking: Showcase simple recipes, cooking techniques, and meal preparation tips.
Food Safety: Provide information on safe food handling practices, storage guidelines, and hygiene.
Personal Well-being: Promote self-care practices, stress management techniques, and mental health awareness.

Target Market(s)

Young adults looking to live independently on their own or with friends

Industry/Entity Type

community services sector

Colors
0054AA
0677BA
7BADD7
CADEEF
E8F1F8

Requirements
Must have
• refer to brief

```html
<!DOCTYPE html>
<html lang="en">
<head>
<meta charset="utf-8">
<title>12 Week Independent Living Skills Program – Flyer</title>
<link href="https://fonts.googleapis.com/css2?family=Montserrat:wght@400;500;700;800&display=swap" rel="stylesheet">
<style>
  :root {
    --brand-deep: #0a3d9c;
    --brand-primary: #0054AA;
    --brand-mid: #0677BA;
    --brand-soft: #7BADD7;
    --brand-pale: #CADEEF;
    --brand-mist: #E8F1F8;
    --ink-navy: #0d2a45;
    --panel: rgba(52, 146, 210, 0.82);
    --white: #ffffff;
    --stage: #ececec;
  }
  * { margin: 0; padding: 0; box-sizing: border-box; }
  html, body {
    width: 1200px; height: 1200px; overflow: hidden;
    background: var(--stage);
    font-family: "Montserrat", Arial, sans-serif;
  }
  .flyer {
    position: absolute; left: 176px; top: 0;
    width: 848px; height: 1200px; overflow: hidden;
    background: var(--brand-deep); color: var(--white);
  }
  .flyer-shapes { position: absolute; inset: 0; }
  .brand {
    position: absolute; left: 505px; top: 46px;
    display: flex; align-items: center; gap: 12px; white-space: nowrap;
  }
  .brand-dot { width: 28px; height: 28px; border-radius: 50%; background: var(--brand-mid); flex: none; }
  .brand-name { font-weight: 700; font-size: 30px; color: var(--ink-navy); letter-spacing: -0.5px; }

  .hero-weeks {
    position: absolute; left: 24px; top: 540px;
    font-weight: 800; font-size: 76px; line-height: 1; letter-spacing: -1px; white-space: nowrap;
  }
  .hero-program {
    position: absolute; left: 33px; top: 626px;
    font-weight: 700; font-size: 34px; line-height: 44px; white-space: nowrap;
  }
  .hero-intro {
    position: absolute; left: 33px; top: 722px; width: 370px;
    font-size: 15px; line-height: 21.5px; font-weight: 500;
  }
  .hero-rule { position: absolute; left: 48px; top: 803px; width: 286px; height: 2px; background: var(--white); }

  .topic { position: absolute; }
  .topic-heading { font-weight: 700; font-size: 21px; line-height: 1.25; letter-spacing: 0.2px; white-space: nowrap; }
  .topic-text { position: absolute; font-size: 15px; line-height: 1.42; font-weight: 500; text-align: center; white-space: nowrap; }
  .icon { position: absolute; fill: none; stroke: var(--white); stroke-width: 2.4; stroke-linecap: round; stroke-linejoin: round; }
</style>
</head>
<body>
<main class="flyer">
  <svg class="flyer-shapes" width="848" height="1200" viewBox="0 0 848 1200">
    <defs>
      <linearGradient id="photoTone" x1="0" y1="0" x2="1" y2="1">
        <stop offset="0" stop-color="#e9e6e1"/>
        <stop offset="0.35" stop-color="#c9b59a"/>
        <stop offset="0.65" stop-color="#bfbfc0"/>
        <stop offset="1" stop-color="#d9d7d4"/>
      </linearGradient>
      <linearGradient id="blueField" x1="0" y1="0" x2="0" y2="1">
        <stop offset="0" stop-color="#0d4fb0"/>
        <stop offset="1" stop-color="#083594"/>
      </linearGradient>
    </defs>
    <rect class="photo" role="img" aria-label="Photo of a smiling young man in a wheelchair using a laptop in a bright living room with a grey sofa" x="0" y="0" width="848" height="620" fill="url(#photoTone)"/>
    <path class="header-swoop" d="M266,0 Q420,150 848,132 L848,0 Z" fill="var(--white)"/>
    <path class="header-band" d="M300,0 Q440,148 848,132 L848,146 Q420,168 290,0 Z" fill="var(--brand-primary)"/>
    <path class="blue-field" d="M0,443 Q280,540 848,611 L848,1200 L0,1200 Z" fill="url(#blueField)"/>
    <polygon points="180,620 360,620 170,1200 0,1200 0,1000" fill="#ffffff" opacity="0.05"/>
    <polygon points="520,650 700,630 560,1200 380,1200" fill="#ffffff" opacity="0.05"/>
    <path class="divider-swoop" d="M0,432 Q300,530 848,555 L848,611 Q280,540 0,443 Z" fill="var(--white)"/>
    <polygon class="panel" points="480,674 848,674 848,824 454,824" fill="var(--panel)"/>
    <polygon class="panel" points="0,834 418,834 394,984 0,984" fill="var(--panel)"/>
    <polygon class="panel" points="434,1002 848,1002 848,1154 410,1154" fill="var(--panel)"/>
  </svg>

  <div class="brand"><span class="brand-dot"></span><span class="brand-name">Brightpath Care</span></div>

  <h1 class="hero-weeks">12 WEEK</h1>
  <h2 class="hero-program">INDEPENDENT LIVING<br>SKILLS PROGRAM</h2>
  <p class="hero-intro">Join our independent living skills program.<br>Enhance the abilities to live independently<br>and confidently.</p>
  <div class="hero-rule"></div>

  <!-- Independent living skills -->
  <svg class="icon" style="left:500px;top:686px" width="58" height="62" viewBox="0 0 58 62">
    <path d="M30,12 C12,10 2,24 4,36 C6,50 22,56 34,52 C40,50 38,44 34,42 C30,40 32,34 38,34 C46,34 50,28 46,22"/>
    <circle cx="14" cy="30" r="4"/><circle cx="20" cy="20" r="4"/><circle cx="16" cy="42" r="4"/><circle cx="26" cy="48" r="3.5"/>
    <path d="M44,4 L52,8 L44,48 L40,46 Z"/><path d="M42,46 L40,56"/>
  </svg>
  <h3 class="topic topic-heading" style="left:578px;top:704px">INDEPENDENT<br>LIVING SKILLS:</h3>
  <p class="topic-text" style="left:460px;top:760px;width:388px">Emphasize the importance of acquiring<br>essential skills for independent living.</p>

  <!-- Food safety -->
  <h3 class="topic topic-heading" style="left:116px;top:867px">FOOD SAFETY:</h3>
  <svg class="icon" style="left:318px;top:842px" width="66" height="66" viewBox="0 0 66 66">
    <path d="M36,10 A26,26 0 1 0 58,38"/><path d="M34,18 A18,18 0 1 0 50,40"/>
    <path d="M30,30 C24,26 18,32 20,40 C22,48 28,50 30,48 C32,50 38,48 40,40 C42,32 36,26 30,30 Z"/><path d="M30,30 L32,24"/>
    <circle cx="50" cy="14" r="10"/><path d="M45,14 L49,18 L55,10"/>
  </svg>
  <p class="topic-text" style="left:0;top:916px;width:412px">Provide information on safe food handling<br>practices, storage guidelines, and hygiene.</p>

  <!-- Money management -->
  <h3 class="topic topic-heading" style="left:488px;top:877px">MONEY MANAGEMENT:</h3>
  <svg class="icon" style="left:760px;top:852px" width="52" height="58" viewBox="0 0 52 58">
    <rect x="4" y="44" width="16" height="8" rx="2"/><rect x="6" y="34" width="14" height="8" rx="2"/><rect x="4" y="24" width="16" height="8" rx="2"/>
    <path d="M26,20 C20,30 22,52 36,52 C50,52 52,30 44,20 Z"/><path d="M28,20 L30,10 L42,10 L44,20"/>
    <path d="M39,28 C33,28 33,35 38,36 C43,37 43,44 36,44 M38,25 L38,47"/>
  </svg>
  <p class="topic-text" style="left:430px;top:924px;width:390px">Highlight budgeting tips, saving<br>strategies, and financial planning.</p>

  <!-- Personal well-being -->
  <h3 class="topic topic-heading" style="left:50px;top:1040px">PERSONAL WELL-BEING:</h3>
  <svg class="icon" style="left:336px;top:1004px" width="60" height="60" viewBox="0 0 60 60">
    <path d="M30,4 C22,12 22,24 30,32 C38,24 38,12 30,4 Z"/>
    <path d="M30,32 C22,32 14,26 14,16 C22,16 28,22 30,32 Z"/><path d="M30,32 C38,32 46,26 46,16 C38,16 32,22 30,32 Z"/>
    <path d="M4,30 L10,48 C18,54 26,54 30,48 C34,54 42,54 50,48 L56,30"/><path d="M12,36 L20,46"/><path d="M48,36 L40,46"/>
  </svg>
  <p class="topic-text" style="left:0;top:1082px;width:426px">Promote self-care practices, stress management<br>techniques, and mental health awareness.</p>

  <!-- Basic cooking -->
  <svg class="icon" style="left:482px;top:1016px" width="66" height="62" viewBox="0 0 66 62">
    <path d="M8,22 L50,22 L48,46 C48,50 44,52 40,52 L18,52 C14,52 10,50 10,46 Z"/>
    <path d="M4,26 L8,26 M50,26 L56,26"/><path d="M6,18 C12,8 46,8 52,18"/><path d="M26,10 L32,10"/>
    <rect x="20" y="30" width="16" height="6" rx="2"/>
    <path d="M58,4 L58,20 M54,4 L54,12 C54,16 62,16 62,12 L62,4"/>
    <path d="M16,58 L42,58"/><path d="M22,54 C20,52 24,50 22,48 M30,54 C28,52 32,50 30,48"/>
  </svg>
  <h3 class="topic topic-heading" style="left:572px;top:1030px">BASIC COOKING:</h3>
  <p class="topic-text" style="left:434px;top:1100px;width:414px">Showcase simple recipes, cooking<br>techniques, and meal preparation tips.</p>
</main>
</body>
</html>
```